1 Page for Computer Repair Website

Looking for a 1 page website with a design that compliments the business card and pamphlet that have already been made (attached files). It should look business professional and easy to read. Email and phone number should be somewhere near the top of the website, visible when the page loads. I don't want any forms for people to mess with. No "Contact Us" form or entering in email for newsletter. Customers will just be looking at this site to confirm we are professionals and have our business in order.

Target Market(s)

Home and small business

Industry/Entity Type

Computer Repair

Coding

Coded - Design and coding required

Number of Pages Required

1 page

Font styles to use
Other font styles liked:
• Helvetica variations used in pamphlet and card

Colors
0455a3
cfdeed
85abd2
3276b5
85cae6
ffffff

Requirements
Must have
• Compliment the pamphlet and business card in color choices and font use. Pleasing to the eye and easy to read through categories and text.
Should not have
• Forms. No "enter name and email here" or anything of the sort.

```html
<!DOCTYPE html>
<html lang="en">
<head>
<meta charset="utf-8">
<title>Fixwell Computer Repair</title>
<link href="https://fonts.googleapis.com/css2?family=Open+Sans:wght@400;600;700&family=Oswald:wght@400;500&display=swap" rel="stylesheet">
<style>
:root{
  --blue:#0455a3;
  --blue-mid:#3276b5;
  --blue-soft:#85abd2;
  --blue-pale:#cfdeed;
  --sky:#85cae6;
  --white:#ffffff;
  --ink:#333b44;
  --muted:#6b747d;
  --rule:#dfe4ea;
  --band:#eef1f4;
  --footer:#2c3238;
}
*{box-sizing:border-box;margin:0;padding:0}
html,body{width:807px;height:1200px;overflow:hidden;background:var(--white)}
body{font-family:"Open Sans",Arial,sans-serif;color:var(--ink);font-size:9px;line-height:1.55}
.page{width:807px;height:1200px;position:relative}

/* header */
.site-header{height:75px;display:flex;align-items:center;justify-content:space-between;padding:0 59px}
.brand{display:flex;align-items:center;gap:7px;font-family:"Oswald",sans-serif;font-size:28px;font-weight:500;color:var(--blue);letter-spacing:1px}
.brand-mark{width:10px;height:10px;background:var(--blue)}
.contacts{display:flex;gap:28px}
.contact{display:flex;align-items:center;gap:8px}
.contact-icon{width:26px;height:26px;border:1px solid var(--blue-soft);border-radius:50%;display:flex;align-items:center;justify-content:center}
.contact-label{font-size:7.5px;font-weight:700;color:var(--ink);letter-spacing:.3px}
.contact-value{font-size:8px;color:var(--muted)}

/* nav */
.main-nav{height:27px;background:var(--blue);display:flex;align-items:center;justify-content:space-between;padding:0 59px}
.main-nav a{color:var(--white);text-decoration:none;font-size:7.5px;font-weight:600;letter-spacing:.4px}

/* hero */
.hero{height:303px;position:relative;overflow:hidden;
  background:radial-gradient(ellipse at 40% 55%,#4f7fa8 0%,#24506f 35%,#0f2b42 75%,#0a1e30 100%)}
.hero-text{position:absolute;right:59px;top:110px;width:300px;color:var(--white)}
.hero-title{font-family:"Oswald",sans-serif;font-size:22px;font-weight:400;letter-spacing:1px;margin-bottom:4px}
.hero-lead{font-size:14px;line-height:1.4;margin-bottom:14px}
.btn{display:inline-block;background:var(--blue);color:var(--white);font-size:7.5px;font-weight:700;letter-spacing:.5px;padding:8px 14px;text-decoration:none}
.hero-cta{position:absolute;right:59px;top:218px}
.hero-arrow{position:absolute;top:145px;width:14px;height:14px}
.hero-dots{position:absolute;bottom:14px;left:50%;transform:translateX(-50%);display:flex;gap:5px}
.hero-dots span{width:6px;height:6px;border-radius:50%;background:var(--blue-soft)}
.hero-dots span.on{background:var(--white)}

/* about */
.about{display:flex;gap:26px;padding:31px 59px 0;height:240px}
.about-photo{width:291px;height:188px;flex:none;background:linear-gradient(135deg,#9fb7cc 0%,#55708a 45%,#2c4257 100%)}
.section-title{font-family:"Oswald",sans-serif;font-size:15px;font-weight:400;letter-spacing:.5px;color:var(--ink);padding-bottom:7px;border-bottom:1px solid var(--rule);margin-bottom:9px}
.about-body p{color:var(--muted);font-size:7.5px;margin-bottom:8px}

/* services */
.services{padding:0 59px;height:335px}
.services-head{display:flex;align-items:center;justify-content:space-between;border-bottom:1px solid var(--rule);padding-bottom:7px;margin-bottom:22px}
.services-head .section-title{border:0;padding:0;margin:0}
.pager{display:flex;gap:4px}
.pager span{width:8px;height:8px;background:var(--rule)}
.service-grid{display:grid;grid-template-columns:repeat(4,1fr);gap:22px}
.service-icon{width:52px;height:52px;border-radius:50%;background:var(--blue-pale);border:2px solid var(--blue-soft);display:flex;align-items:center;justify-content:center;margin:0 auto 12px}
.service-name{font-size:8px;font-weight:700;color:var(--ink);margin-bottom:5px}
.service-text{font-size:7px;color:var(--muted);margin-bottom:6px}
.read-more{font-size:7px;font-weight:700;color:var(--blue);text-decoration:none}

/* why */
.why{background:var(--band);height:180px;padding:14px 98px 0}
.why .section-title{border:0;padding:0;margin-bottom:14px;font-size:13px}
.why-list{display:grid;grid-template-columns:1fr 1fr;column-gap:40px;row-gap:12px;list-style:none}
.why-list li{display:flex;gap:8px;font-size:7px;color:var(--muted)}
.why-list li::before{content:"";flex:none;width:5px;height:5px;border-radius:50%;background:var(--blue);margin-top:3px}

/* footer */
.site-footer{position:absolute;bottom:0;left:0;right:0;height:43px;background:var(--footer);color:#a8b0b8;font-size:7px;display:flex;align-items:center;justify-content:center}
</style>
</head>
<body>
<div class="page">

  <header class="site-header">
    <div class="brand"><span class="brand-mark"></span>FIXWELL</div>
    <div class="contacts">
      <div class="contact">
        <span class="contact-icon"><svg width="13" height="10" viewBox="0 0 13 10"><rect x="0.5" y="0.5" width="12" height="9" fill="none" stroke="#0455a3"/><path d="M.5 .5 6.5 5.5 12.5 .5" fill="none" stroke="#0455a3"/></svg></span>
        <div><div class="contact-label">EMAIL WHEN YOU NEED US</div><div class="contact-value">info@fixwellpc.com</div></div>
      </div>
      <div class="contact">
        <span class="contact-icon"><svg width="10" height="13" viewBox="0 0 10 13"><rect x="1" y="0.5" width="8" height="12" rx="1.5" fill="none" stroke="#0455a3"/><circle cx="5" cy="10.3" r=".8" fill="#0455a3"/></svg></span>
        <div><div class="contact-label">PHONE</div><div class="contact-value">0772 - 555 - 0148</div></div>
      </div>
    </div>
  </header>

  <nav class="main-nav">
    <a href="#">HOME</a><a href="#">ABOUT US</a><a href="#">OUR SERVICES</a><a href="#">PHOTO GALLERY</a><a href="#">BLOG</a><a href="#">TESTIMONIALS</a><a href="#">CONTACT US</a>
  </nav>

  <section class="hero" role="img" aria-label="Hand reaching toward glowing digital icons in front of a server room">
    <svg class="hero-arrow" style="left:20px" viewBox="0 0 14 14"><path d="M9 2 4 7l5 5" fill="none" stroke="#fff" stroke-width="1.5"/></svg>
    <svg class="hero-arrow" style="right:20px" viewBox="0 0 14 14"><path d="M5 2l5 5-5 5" fill="none" stroke="#fff" stroke-width="1.5"/></svg>
    <div class="hero-text">
      <h1 class="hero-title">LOREM IPSUM DOLOR SIT AMET</h1>
      <p class="hero-lead">Modus quando eum ad, commodo maiestatis est ut, nemore aperiam meliore cu nec. Quo ad</p>
    </div>
    <a class="btn hero-cta" href="#">GET A QUOTE</a>
    <div class="hero-dots"><span class="on"></span><span></span><span></span></div>
  </section>

  <section class="about">
    <div class="about-photo" role="img" aria-label="Technician with a laptop working beside server racks"></div>
    <div class="about-body">
      <h2 class="section-title">ABOUT OUR FIXWELL</h2>
      <p>Lorem ipsum dolor sit amet, nullam praesent ut tation vivendo at, qui ne putent definiebas. Eum sumo persius adversarium id, nam et viderer consulatu instructior.</p>
      <p>Ne quas minim mei, vix eu elitr tollit vocibus, amet fierent detraxit per ne. Usu ut error appetere, ut possim graeci mediocritatem duo, cum ex vero nostrud.</p>
      <p>Id quo wisi iusto electram, sit dicta regione an, ut vero ludus soleat duo. Has eu nibh populo.</p>
      <a class="btn" href="#">MORE ABOUT US</a>
    </div>
  </section>

  <section class="services">
    <div class="services-head">
      <h2 class="section-title">OUR SERVICES</h2>
      <div class="pager"><span></span><span></span></div>
    </div>
    <div class="service-grid">
      <article class="service">
        <div class="service-icon"><svg width="24" height="24" viewBox="0 0 24 24"><path d="M12 2 4 5v6c0 5 3.5 9 8 11 4.5-2 8-6 8-11V5z" fill="none" stroke="#0455a3" stroke-width="2"/><path d="M8 12l3 3 5-6" fill="none" stroke="#0455a3" stroke-width="2"/></svg></div>
        <h3 class="service-name">MALWARE REMOVAL</h3>
        <p class="service-text">Modus quando eum commodo maiestatis est ut, nemore aperiam meliore cu nec quo ad.</p>
        <a class="read-more" href="#">READ MORE »</a>
      </article>
      <article class="service">
        <div class="service-icon"><svg width="24" height="24" viewBox="0 0 24 24"><path d="M5 19 15 9M19 5l-3 3M4 4l6 6M14 14l6 6" fill="none" stroke="#0455a3" stroke-width="2.2" stroke-linecap="round"/></svg></div>
        <h3 class="service-name">PC / LAPTOP REPAIR</h3>
        <p class="service-text">Modus quando eum commodo maiestatis est ut, nemore aperiam meliore cu nec quo ad.</p>
        <a class="read-more" href="#">READ MORE »</a>
      </article>
      <article class="service">
        <div class="service-icon"><svg width="24" height="24" viewBox="0 0 24 24"><rect x="3" y="7" width="18" height="10" rx="1.5" fill="none" stroke="#0455a3" stroke-width="2"/><circle cx="16" cy="12" r="1.6" fill="#0455a3"/><path d="M6 12h6" stroke="#0455a3" stroke-width="2"/></svg></div>
        <h3 class="service-name">HARDWARE / SOFTWARE UPGRADE</h3>
        <p class="service-text">Modus quando eum commodo maiestatis est ut, nemore aperiam meliore cu nec quo ad.</p>
        <a class="read-more" href="#">READ MORE »</a>
      </article>
      <article class="service">
        <div class="service-icon"><svg width="24" height="24" viewBox="0 0 24 24"><rect x="3" y="4" width="18" height="12" rx="1" fill="none" stroke="#0455a3" stroke-width="2"/><path d="M9 20h6M12 16v4M8 10h8M13 7l3 3-3 3" fill="none" stroke="#0455a3" stroke-width="2"/></svg></div>
        <h3 class="service-name">DATA MIGRATION</h3>
        <p class="service-text">Modus quando eum commodo maiestatis est ut, nemore aperiam meliore cu nec quo ad.</p>
        <a class="read-more" href="#">READ MORE »</a>
      </article>
    </div>
  </section>

  <section class="why">
    <h2 class="section-title">WHY CHOOSE US</h2>
    <ul class="why-list">
      <li>Lorem ipsum dolor sit amet, nullam praesent ut tation vivendo at, qui ne putent definiebas ut.</li>
      <li>Lorem ipsum dolor sit amet, nullam praesent ut tation vivendo at, qui ne putent definiebas ut.</li>
      <li>Lorem ipsum dolor sit amet, nullam praesent ut tation vivendo at, qui ne putent definiebas ut.</li>
      <li>Lorem ipsum dolor sit amet, nullam praesent ut tation vivendo at, qui ne putent definiebas ut.</li>
      <li>Lorem ipsum dolor sit amet, nullam praesent ut tation vivendo at, qui ne putent definiebas ut.</li>
      <li>Lorem ipsum dolor sit amet, nullam praesent ut tation vivendo at, qui ne putent definiebas ut.</li>
    </ul>
  </section>

  <footer class="site-footer">All Rights Reserved · Copyright 2024 Fixwell Computer Repair</footer>
</div>
</body>
</html>
```